Logo/stationary needed for a Holding Company

Hello I need a logo for my holding company, Pinegrove Capital, LLC. I would like it VERY clean and professional. I am thinking similar to a law firm or financial company. I would appreciate stationary/envelope as well under the address below. Thank you very much.

2876 North 47th Avenue
Upper Suite
Maple Ridge, Ohio 44718

Target Market(s)

Irrelevant for this project

Industry/Entity Type

It Company

Logo Text

Pinegrove Capital, LLC or Pinegrove Capital

Logo styles of interest
Wordmark Logo
Lettermark Logo
Font styles to use
Serif
Sans Serif

Colors
0293ce
0355a3
3277b5
34a7d8
85cae6
85acd3
cee9f5

Requirements
Must have
• company name
Nice to have
• just very clean and professional
Should not have
• n/a

```html
<!DOCTYPE html>
<html lang="en">
<head>
<meta charset="utf-8">
<title>Pinegrove Capital — Stationery</title>
<link rel="stylesheet" href="https://fonts.googleapis.com/css2?family=Marcellus&family=Marcellus+SC&family=Open+Sans:wght@400&display=swap">
<style>
  :root {
    --blue-deep: #0355a3;
    --blue-mid: #3277b5;
    --blue-bright: #0293ce;
    --blue-light: #85cae6;
    --blue-pale: #cee9f5;
    --paper: #ffffff;
    --paper-shade: #f1f2f4;
    --ink: #3a3a3a;
    --ink-soft: #6b6b6b;
    --rule: #8a8a8a;
    --backdrop: #e4e6ea;
  }
  * { box-sizing: border-box; margin: 0; padding: 0; }
  html, body { width: 1200px; height: 840px; overflow: hidden; }
  body { background: var(--backdrop); position: relative; font-family: "Open Sans", sans-serif; }

  .wordmark {
    font-family: "Marcellus", serif;
    color: var(--blue-mid);
    text-transform: uppercase;
    line-height: 1.05;
    display: inline-block;
    text-align: center;
    white-space: nowrap;
  }
  .wordmark span { display: block; }

  .address {
    font-family: "Marcellus SC", serif;
    color: var(--ink);
    line-height: 1.35;
    white-space: nowrap;
  }

  /* Envelope with open flap */
  .envelope-back {
    position: absolute; left: 40px; top: 60px; width: 520px; height: 330px;
  }
  .envelope-back .flap {
    position: absolute; left: 0; top: 0; width: 520px; height: 80px;
    background: var(--blue-deep);
    clip-path: polygon(0 100%, 6% 0, 94% 0, 100% 100%);
  }
  .envelope-back .body {
    position: absolute; left: 0; top: 80px; width: 520px; height: 250px;
    background: var(--paper);
    box-shadow: 0 6px 18px rgba(0,0,0,.12);
    display: flex; align-items: center; padding-left: 70px; gap: 22px;
  }
  .envelope-back .body::before {
    content: ""; position: absolute; left: 0; top: 0; right: 0; height: 34px;
    background: linear-gradient(var(--blue-mid), var(--blue-bright));
    clip-path: polygon(0 0, 100% 0, 96% 100%, 4% 100%);
    opacity: .85;
  }
  .envelope-back .wordmark { font-size: 24px; }
  .divider { width: 1px; height: 62px; background: var(--rule); }
  .envelope-back .address { font-size: 14px; }

  /* Window envelope */
  .envelope-front {
    position: absolute; left: 40px; top: 440px; width: 520px; height: 260px;
    background: var(--paper);
    box-shadow: 0 6px 18px rgba(0,0,0,.12);
    border-left: 14px solid var(--blue-deep);
  }
  .envelope-front .window {
    position: absolute; left: 50px; top: 60px; width: 300px; height: 120px;
    border-radius: 10px;
    background: var(--paper-shade);
    border: 1px solid #d8dbe0;
    display: flex; align-items: center; padding-left: 22px; gap: 14px;
  }
  .envelope-front .wordmark { font-size: 17px; }
  .envelope-front .divider { height: 50px; }
  .envelope-front .address { font-size: 12px; }

  /* Letterhead */
  .letterhead {
    position: absolute; left: 610px; top: 30px; width: 552px; height: 780px;
    background: var(--paper);
    box-shadow: 0 8px 24px rgba(0,0,0,.14);
    padding: 56px 70px 0 64px;
  }
  .letterhead .edge-band {
    position: absolute; right: 0; top: 0; width: 16px; height: 100%;
    background: linear-gradient(var(--blue-light) 0 22%, var(--blue-deep) 22% 60%, var(--blue-mid) 60% 100%);
  }
  .letterhead .wordmark { font-size: 22px; }
  .letter-body {
    margin-top: 34px; font-size: 9px; line-height: 1.55; color: var(--ink);
  }
  .letter-body p { margin-bottom: 9px; }
  .letterhead .address {
    position: absolute; left: 64px; top: 470px; font-size: 10px; text-align: center;
  }
</style>
</head>
<body>

  <section class="envelope-back" aria-label="Envelope, flap open">
    <div class="flap"></div>
    <div class="body">
      <div class="wordmark"><span>Pinegrove</span><span>Capital</span></div>
      <div class="divider"></div>
      <div class="address">2876 North 47th Avenue<br>Upper Suite<br>Maple Ridge, Ohio 44718</div>
    </div>
  </section>

  <section class="envelope-front" aria-label="Window envelope">
    <div class="window">
      <div class="wordmark"><span>Pinegrove</span><span>Capital</span></div>
      <div class="divider"></div>
      <div class="address">2876 North 47th Avenue<br>Upper Suite<br>Maple Ridge, Ohio 44718</div>
    </div>
  </section>

  <article class="letterhead" aria-label="Letterhead">
    <div class="edge-band"></div>
    <header class="wordmark"><span>Pinegrove</span><span>Capital</span></header>
    <div class="letter-body">
      <p>Thank you for your continued trust in our firm. This letter confirms the terms discussed at our recent meeting and outlines the next steps for the coming quarter.</p>
      <p>Our team has reviewed the holdings under management and prepared a summary of current positions, expected returns and scheduled distributions. The attached report sets out each item in detail, along with the supporting figures requested by your office.</p>
      <p>Please review the enclosed documents at your convenience. Should any questions arise, our partners are available to meet in person or by phone to walk through the figures and answer any concerns you may have.</p>
      <p>We look forward to another productive year together and to building lasting value for every stakeholder.</p>
    </div>
    <footer class="address">2876 North 47th Avenue<br>Upper Suite<br>Maple Ridge, Ohio 44718</footer>
  </article>

</body>
</html>
```